Special release wine label

Marrow Creek Vineyards is a small premium wine producer in the Barossa - South Australia. We are a five star rated winery, producing exceptional wines true to variety, region and house style. We have a very special parcel of wine that we wish to release as an exclusive wine. Visit www.marrowcreekvineyards.com.au for further feel.

The wine will be called Marrow Creek Vineyards, 2012, The Quiet Harvest Shiraz - Cabernet.

The wine can be bottled in either a burgundy or Bordeaux shaped bottle

Industry/Entity Type

House

```html
<!DOCTYPE html>
<html lang="en">
<head>
<meta charset="utf-8">
<title>Marrow Creek – The Quiet Harvest Shiraz Cabernet 2012 Label</title>
<link href="https://fonts.googleapis.com/css2?family=Cinzel:wght@500&family=Norican&family=Playfair+Display:wght@700&display=swap" rel="stylesheet">
<style>
  :root {
    --backdrop: #ebebeb;
    --paper: #ece7dc;
    --paper-stain: #d9ceb8;
    --paper-shade: #c9c2b4;
    --band: #2a2a2a;
    --band-text: #ffffff;
    --wine-red: #a0161c;
    --ink: #111111;
    --label-white: #ffffff;
  }

  * { margin: 0; padding: 0; box-sizing: border-box; }

  html, body {
    width: 1200px;
    height: 987px;
    overflow: hidden;
    background: var(--backdrop);
  }

  .label {
    position: absolute;
    left: 281px;
    top: 41px;
    width: 638px;
    height: 905px;
    background: var(--paper);
    overflow: hidden;
  }

  .artwork {
    position: absolute;
    left: 0;
    width: 100%;
    background:
      radial-gradient(ellipse 40% 30% at 80% 25%, var(--paper-stain), transparent 70%),
      radial-gradient(ellipse 30% 55% at 50% 65%, var(--paper-shade), transparent 75%),
      var(--paper);
  }
  .artwork--top { top: 0; height: 223px; }
  .artwork--reflection { top: 689px; height: 216px; transform: scaleY(-1); }

  .name-band {
    position: absolute;
    left: 0;
    width: 100%;
    height: 98px;
    background: var(--band);
    display: flex;
    align-items: center;
    justify-content: center;
  }
  .name-band--top { top: 222px; }
  .name-band--reflection { top: 590px; }

  .winery-name {
    font-family: "Cinzel", serif;
    font-weight: 500;
    font-size: 40px;
    letter-spacing: 2px;
    color: var(--band-text);
  }
  .name-band--top .winery-name { margin-top: 10px; }
  .name-band--reflection .winery-name {
    transform: scaleY(-1);
    margin-bottom: 10px;
  }

  .title-panel {
    position: absolute;
    left: 0;
    top: 320px;
    width: 100%;
    height: 270px;
    background: var(--label-white);
    text-align: center;
  }

  .wine-article,
  .wine-name,
  .wine-variety {
    font-family: "Norican", cursive;
    color: var(--wine-red);
    font-weight: 400;
  }
  .wine-article {
    display: block;
    font-size: 44px;
    line-height: 1;
    padding-top: 20px;
  }
  .wine-name {
    display: block;
    font-size: 52px;
    line-height: 1;
    margin-top: 2px;
  }
  .wine-variety {
    display: block;
    font-size: 76px;
    line-height: 1;
    margin-top: 6px;
  }
  .vintage {
    display: block;
    font-family: "Playfair Display", serif;
    font-weight: 700;
    font-size: 40px;
    line-height: 1;
    color: var(--ink);
    margin-top: 0;
  }
</style>
</head>
<body>
  <main class="label">
    <div class="artwork artwork--top" role="img" aria-label="Sketched homestead with three tall palm trees on aged paper"></div>

    <div class="name-band name-band--top">
      <span class="winery-name">MARROW CREEK</span>
    </div>

    <section class="title-panel">
      <h1>
        <span class="wine-article">the</span>
        <span class="wine-name">Quiet Harvest Shiraz</span>
        <span class="wine-variety">- Cabernet -</span>
      </h1>
      <span class="vintage">2012</span>
    </section>

    <div class="name-band name-band--reflection" aria-hidden="true">
      <span class="winery-name">MARROW CREEK</span>
    </div>

    <div class="artwork artwork--reflection" role="img" aria-label="Mirrored reflection of the homestead and palm trees on aged paper"></div>
  </main>
</body>
</html>
```